All-natural soap packaging design for new company

The box type has been selected, we just need artwork for each of our 10 products. I'd like the same look to each, the idea is just to switch out the name and ingredient label on each. The dimensions are 3.5"x3.75"x1.25". The colors in the uploaded pictures with product titles are not mandatory. I'd like to keep the font on the packaging (Rubik) as it is the same as the website.

Target Market(s)

Health & Beauty, people looking for natural or organic products

Industry/Entity Type

It Company

Colors

Designer to choose colors to be used in the design.

Requirements
Must have
• Design must be clean and relatively simple. Slightly different look for each of the 10 products. Audience is people looking for all-natural products.

```html
<!DOCTYPE html>
<html lang="en">
<head>
<meta charset="utf-8">
<title>Organic Lemongrass with Jojoba – Soap Box Front</title>
<link rel="stylesheet" href="https://fonts.googleapis.com/css2?family=Oswald:wght@500;700&family=Rubik:wght@400;500&display=swap">
<style>
  :root {
    --page-bg: #e4e4e4;
    --box-green: #7cc63a;
    --box-green-deep: #4fa52a;
    --box-light: #eef7e6;
    --label-bg: #c8cebf;
    --label-border: #f7f8f4;
    --ink-green: #4d6a37;
    --ink-body: #4a5640;
    --banner: #a6a880;
    --banner-light: #b3b58f;
    --rule: #f4f5f0;
  }
  html, body {
    margin: 0;
    width: 1200px;
    height: 935px;
    overflow: hidden;
    background: var(--page-bg);
  }
  .box-front {
    position: absolute;
    left: 220px;
    top: 57px;
    width: 760px;
    height: 820px;
    overflow: hidden;
  }
  .box-art {
    position: absolute;
    inset: 0;
    background:
      radial-gradient(ellipse at 50% 0%, var(--box-light) 0%, rgba(238,247,230,0.6) 22%, rgba(238,247,230,0) 45%),
      linear-gradient(180deg, #d9eec6 0%, #a6d976 30%, var(--box-green) 60%, var(--box-green-deep) 100%);
  }
  .label {
    position: absolute;
    left: 92px;
    top: 112px;
    width: 585px;
    height: 607px;
    box-sizing: border-box;
    background: var(--label-bg);
    border: 5px solid var(--label-border);
    font-family: "Rubik", sans-serif;
    color: var(--ink-body);
  }
  .label > * { position: absolute; }
  .organic-tag {
    left: 214px; top: 38px;
    width: 144px; height: 58px;
    box-sizing: border-box;
    border: 2px solid var(--ink-green);
    outline: 1px solid var(--ink-green);
    outline-offset: -6px;
    display: flex; align-items: center; justify-content: center;
    font-family: "Oswald", sans-serif;
    font-weight: 700;
    font-size: 30px;
    color: var(--ink-green);
    letter-spacing: 0.5px;
  }
  .organic-line {
    top: 66px; height: 2px; width: 100px;
    background: var(--ink-green);
  }
  .organic-line.left { left: 102px; }
  .organic-line.right { left: 370px; }
  .product-name {
    left: 0; right: 0; top: 118px;
    margin: 0;
    text-align: center;
    font-family: "Oswald", sans-serif;
    font-weight: 700;
    font-size: 78px;
    line-height: 1;
    letter-spacing: -1px;
    color: var(--ink-green);
    transform: scaleX(0.88);
  }
  .title-dot-line {
    left: 235px; top: 206px; width: 105px; height: 2px;
    background: var(--rule);
  }
  .ribbon {
    left: 92px; top: 218px;
    width: 392px; height: 80px;
    background: linear-gradient(90deg, var(--banner) 0%, var(--banner-light) 50%, var(--banner) 100%);
    display: flex; align-items: center; justify-content: center;
    font-size: 30px;
    color: #ffffff;
    letter-spacing: 1px;
  }
  .tag-rule {
    left: 60px; right: 60px; top: 352px;
    height: 3px;
    background: var(--rule);
  }
  .tag-rule-cap {
    top: 340px; width: 3px; height: 26px; background: var(--rule);
  }
  .tag-rule-cap.left { left: 60px; }
  .tag-rule-cap.right { right: 60px; }
  .benefit-tag {
    left: 136px; top: 334px;
    width: 308px; height: 40px;
    background: var(--ink-green);
    color: #f2f4ee;
    font-family: "Oswald", sans-serif;
    font-weight: 500;
    font-size: 19px;
    display: flex; align-items: center; justify-content: center;
    letter-spacing: -0.2px;
  }
  .benefit-copy {
    top: 422px; width: 172px;
    margin: 0;
    text-align: center;
    text-transform: uppercase;
    font-size: 13px;
    line-height: 17px;
  }
  .benefit-copy.left { left: 14px; }
  .benefit-copy.right { left: 384px; }
  .column-rule {
    top: 402px; height: 132px; width: 2px;
    background: var(--rule);
  }
  .column-rule.a { left: 196px; }
  .column-rule.b { left: 203px; }
  .column-rule.c { left: 370px; }
  .column-rule.d { left: 377px; }
  .brand {
    left: 220px; top: 398px;
    width: 140px; height: 138px;
    display: flex; flex-direction: column; align-items: center; justify-content: center; gap: 12px;
  }
  .brand-square {
    width: 44px; height: 44px;
    background: var(--ink-green);
  }
  .brand-name {
    font-size: 14px;
    font-weight: 500;
    color: var(--ink-green);
    text-transform: uppercase;
    text-align: center;
    line-height: 1.2;
  }
  .base-rule {
    left: 60px; right: 60px; top: 556px;
    height: 3px; background: var(--rule);
  }
  .base-rule-cap { top: 546px; width: 3px; height: 22px; background: var(--rule); }
  .base-rule-cap.left { left: 60px; }
  .base-rule-cap.right { right: 60px; }
  .net-weight {
    left: 0; right: 0; top: 570px;
    text-align: center;
    font-size: 18px;
    color: var(--ink-body);
  }
</style>
</head>
<body>
  <section class="box-front">
    <div class="box-art" role="img" aria-label="Green soap foam bubbles and lemongrass leaf texture background"></div>

    <div class="label">
      <span class="organic-line left"></span>
      <div class="organic-tag">ORGANIC</div>
      <span class="organic-line right"></span>

      <h1 class="product-name">LEMONGRASS</h1>
      <span class="title-dot-line"></span>

      <div class="ribbon" role="img" aria-label="Decorative ribbon banner reading With Jojoba"><span>WITH JOJOBA</span></div>

      <span class="tag-rule"></span>
      <span class="tag-rule-cap left"></span>
      <span class="tag-rule-cap right"></span>
      <div class="benefit-tag">SOOTHING, ASTRINGENT &amp; ANTIFUNGAL</div>

      <p class="benefit-copy left">Lemongrass oil improves skin tone, reduces enlarged pores and excessive sweating of skin.</p>

      <span class="column-rule a"></span>
      <span class="column-rule b"></span>
      <div class="brand">
        <span class="brand-square"></span>
        <span class="brand-name">Marlow Soap Co.</span>
      </div>
      <span class="column-rule c"></span>
      <span class="column-rule d"></span>

      <p class="benefit-copy right">Jojoba oil cleanses clogged pores and restores the skin’s natural pH balance.</p>

      <span class="base-rule"></span>
      <span class="base-rule-cap left"></span>
      <span class="base-rule-cap right"></span>
      <div class="net-weight">Net Wt. 3.25 oz ( 92 GM )</div>
    </div>
  </section>
</body>
</html>
```